Web design for new streaming audio service

We need a homepage design for a new streaming audio service. Our company is called Lumawave, and we’re basically Reelcove for Audiobooks, Stand-Up Comedy, Lectures, Language Learning, etc. Essentially like Tunevast for everything audio EXCEPT music.
You don’t have to code the homepage (Design Only), but it should include 3 different designs to work with 1) Web; 2) Phones; 3) Tablets.
Below is a link to a mockup of the web version which gives a good idea of what elements we want. This is just a mockup and we want you to improve it.
Once you download the mockup, please refer to the more detailed instructions below:
The following outlines the design project for the Lumawave homepage. We have provided a rough mockup of the homepage layout that gives you a general idea of what we’re going for. There are a few elements that we are attached to, and many others where you have complete creative freedom to do whatever you think looks good.
The ZIP file includes the following:
* Mockup to see what we have in mind (lumawave-homepage-mockup.jpg)
* Text used (lumawave-homepage-text.txt)
* Raw image of actor (lumawave-actor1.jpg)
* Raw images for samples (lumawave-sample-[name].jpg)
Although we have only provided a mockup layout for the web version, we also need you to provide a mobile phone and a tablet version of the design also. It’s very possible the tablet version may be substantially similar to the web version, but the mobile phone version will likely be much different.
All of the raw files are included in the attached ZIP file. Please use our photographs and text as provided although cropping, sizing, etc. is flexible per the instructions below.
Display Requirements:
* Web Version - Minimum resolution 1024x768 (72 dpi) but should look good on 1920x1080 (72 dpi) - Page should be designed to scale to look acceptable in all resolutions in between.
* Phone Version - Minimum Zelphone 4 - 640x960 (326 dpi) but should look good on Ordano Vexa T3 - 1920x1080 (441 dpi) - Page should be designed to scale to look acceptable in all resolutions and devices in between.
* Tablet Version - Minimum Pagelit Ember QX 7” - 1280x800 (216 dpi) but should also look good on a Tabrel Wisp - 2048x1536 (264 dpi) - Page should be designed to scale to look acceptable in all resolutions and devices in between.
Above the Fold - We want to make sure the Lumawave logo, Member Login Link, Large Photo, Headline, Price, Button, and the first row of sample images are all “Above the fold”. As a general guideline, this means 600 pixels high on a 1024x768 72 dpi web screen. This requirement is less important on Phone versions.
Top Logo Bar - We want to retain the blue bar with the Lumawave logo on the page, although we are open to a different size, shape and positioning if it greatly enhances the design. Please use the standard logo color, although you are welcome to use either the horizontal or vertical orientation of the logo based on your design.
Text color, font and size - Feel free to design the text in anyway you choose as long as the text is readable on the target platforms.
Buttons - Feel free to use any size, shape and colors for the buttons as long as they are obvious and clickable relative to the page. The only exception is the Chatterly button should follow the Chatterly color scheme and logo treatment (the mockup doesn’t seem 100% correct.)
Top Photograph - We want to retain the large photograph across the top of the screen although final shape and dimensions are flexible.
Size and shape of content samples (i.e. Audiobooks, Stand-Up Comedy, etc.) - Feel free to design the content samples in anyway you choose.
Three Sales Points (i.e. Listen on your Zelphone…, All you can enjoy…, etc.) - The Three Sales Points are envisioned to each have a corresponding illustration which you should provide and have rights for. The placeholder is represented by a square next to the text. The color size and shape of these elements are flexible and can be designed in any way you choose.
Opt-in form - Feel free to design the opt-in form in anyway you choose as long as the text is readable and the interactivity is obvious on the target platforms.
Text links and copyright notice - Feel free to design the bottom of the page text links and copyright notice in anyway you choose.
Additional colors, graphic design elements, etc. - Feel free to use any additional colors, graphic design elements, etc. to support your design.
Target Market(s)
people who want to listen to audio through their mobile devices.
Industry/Entity Type
Graphic Design
Look and feel

```html
<!DOCTYPE html>
<html lang="en">
<head>
<meta charset="utf-8">
<title>Lumawave — Unlimited listening</title>
<link href="https://fonts.googleapis.com/css2?family=PT+Sans:ital,wght@0,400;0,700;1,400&family=Ubuntu:wght@400;500;700&display=swap" rel="stylesheet">
<style>
:root{
  --orange:#fbab18;
  --orange-deep:#f28a1e;
  --ink:#2b2b2b;
  --band:#353535;
  --text:#333333;
  --muted:#8d8d8d;
  --rule:#d6d6d6;
  --chat-blue:#3b5998;
  --chat-blue-dark:#30497d;
  --hex-blue:#2f6f97;
  --white:#ffffff;
}
*{margin:0;padding:0;box-sizing:border-box}
html,body{width:1200px;height:2211px;overflow:hidden;background:var(--white)}
body{position:relative;font-family:"PT Sans",Arial,sans-serif;color:var(--text)}
.abs{position:absolute}

/* hero */
.hero-photo{left:0;top:21px;width:1200px;height:772px;
  background:
    radial-gradient(ellipse 520px 520px at 760px 330px,#c59274 0%,#b0876e 30%,rgba(176,135,110,0) 70%),
    linear-gradient(180deg,rgba(0,0,0,0) 55%,#5c6a86 100%),
    linear-gradient(90deg,#f7f3ee 0%,#f2ebe3 30%,#d9c3ae 55%,#9c8471 80%,#d8cbbd 100%);}
.hero-rule{left:0;top:793px;width:1200px;height:4px;background:var(--orange)}
.topbar{left:19px;top:21px;width:1161px;height:97px;background:var(--ink);border-top:3px solid var(--orange)}
.brand{left:44px;top:45px;display:flex;align-items:center;gap:14px;color:var(--white);font-weight:700;font-size:44px;line-height:1}
.brand-dot{width:40px;height:40px;border-radius:50%;background:var(--white)}
.member-login{left:939px;top:21px;width:206px;height:50px;background:var(--orange);color:var(--white);
  font-family:"Ubuntu",sans-serif;font-weight:500;font-size:19px;display:flex;align-items:center;justify-content:center;
  border-radius:0 0 8px 8px}
.headline{left:41px;top:244px;font-family:"Ubuntu",sans-serif;color:var(--orange);font-size:56px;line-height:65px}
.headline b{font-weight:700;display:block}
.headline span{font-weight:400;display:block}
.price{left:41px;top:377px;font-size:28px;color:var(--text)}
.btn-trial{left:41px;top:433px;width:304px;height:53px;background:var(--ink);border:2px solid #111;border-radius:4px;
  color:var(--white);font-family:"Ubuntu",sans-serif;font-weight:500;font-size:23px;display:flex;align-items:center;justify-content:center}
.note{left:41px;top:502px;font-size:15px;color:var(--orange-deep)}

/* section titles */
.section-title{display:flex;align-items:center;gap:18px;font-size:29px;color:var(--text)}
.section-title::before,.section-title::after{content:"";flex:1;height:4px;border-top:1px solid var(--rule);border-bottom:1px solid var(--rule)}
.samples-title{left:19px;top:825px;width:1161px}
.samples-title::before{display:none}

/* samples */
.sample{width:268px}
.sample .cover{height:188px}
.sample .name{margin-top:10px;text-align:center;font-size:18px;color:var(--text)}
.sample .sub{text-align:center;font-size:13px;color:var(--muted);margin-top:1px}
.sample .line{margin-top:9px;height:3px;background:var(--rule)}
.sample.active .name{color:var(--orange)}
.sample.active .line{background:var(--orange)}

/* sales points */
.band{left:0;top:1455px;width:1200px;height:281px;background:var(--band)}
.point{top:1523px;width:345px;height:174px;background:var(--white);text-align:center;padding:50px 24px 0}
.point.featured{background:var(--orange);color:var(--white)}
.point h3{font-weight:400;font-size:19px;line-height:23px}
.point p{font-size:13.5px;line-height:21px;color:var(--muted);margin-top:8px}
.point.featured p{color:var(--white)}
.hex{top:1484px;width:62px;height:70px}

/* opt-in */
.trial-title{left:19px;top:1772px;width:1161px}
.pitch{left:0;top:1843px;width:1200px;text-align:center;font-size:22px;line-height:31px;color:var(--muted)}
.pitch-strong{left:0;top:1922px;width:1200px;text-align:center;font-size:19px;font-weight:700;color:var(--text)}
.email{left:252px;top:1971px;width:700px;height:53px;border:2px solid #e3e3e3;border-radius:3px;
  font-style:italic;font-size:16px;color:#b5b5b5;padding:15px 10px}
.btn-access{left:252px;top:2065px;width:292px;height:53px;border-radius:3px;
  background:linear-gradient(180deg,#f9a23b,var(--orange-deep));color:var(--white);font-weight:700;font-size:19px;
  display:flex;align-items:center;justify-content:center}
.or{left:560px;top:2080px;width:84px;text-align:center;font-size:16px;color:var(--muted)}
.btn-chat{left:660px;top:2065px;width:294px;height:53px;border-radius:3px;background:var(--chat-blue);color:var(--white);
  font-weight:700;font-size:19px;display:flex;align-items:center;overflow:hidden}
.btn-chat .mark{width:47px;height:53px;background:var(--chat-blue-dark);margin-right:14px}

/* footer */
.footer{left:0;top:2157px;width:1200px;height:54px;background:var(--band);color:#c9c9c9;font-size:15px;
  display:flex;align-items:center;justify-content:space-between;padding:0 19px}
.footer nav span{margin:0 8px}
.footer nav span:first-child{margin-left:0}
</style>
</head>
<body>

<div class="abs hero-photo" role="img" aria-label="Smiling young man wearing headphones, looking at his phone, on a bright blurred home background"></div>
<div class="abs hero-rule"></div>

<header class="abs topbar"></header>
<div class="abs brand"><span class="brand-dot"></span>Lumawave</div>
<div class="abs member-login">MEMBER LOGIN</div>

<h1 class="abs headline"><b>Unlimited listening.</b><span>Wherever you are.</span></h1>
<div class="abs price">Only $9.99 per month</div>
<div class="abs btn-trial">START YOUR FREE TRAIL</div>
<div class="abs note">*Credit Card Not Required</div>

<h2 class="abs section-title samples-title">A Sample of what you can listen to on lumawave</h2>

<div class="abs sample active" style="left:19px;top:895px">
  <div class="cover" role="img" aria-label="Audiobook cover: noir suspense novels" style="background:linear-gradient(135deg,#2d2d2d,#8a8a8a 50%,#1c1c1c)"></div>
  <div class="name">Audio Books</div><div class="sub">Lorem ipsum</div><div class="line"></div>
</div>
<div class="abs sample" style="left:317px;top:895px">
  <div class="cover" role="img" aria-label="Stand-up comedy album cover with a boxing ring" style="background:linear-gradient(160deg,#8e8a86,#6f6761 60%,#b9aea3)"></div>
  <div class="name">Stand-Up Comedy</div><div class="sub">Lorem ipsum</div><div class="line"></div>
</div>
<div class="abs sample" style="left:613px;top:895px">
  <div class="cover" role="img" aria-label="French language course cover" style="background:linear-gradient(180deg,#101828 0 24%,#1aa6dc 24% 100%)"></div>
  <div class="name">Language Learning</div><div class="sub">Lorem ipsum</div><div class="line"></div>
</div>
<div class="abs sample" style="left:911px;top:895px">
  <div class="cover" role="img" aria-label="Memoir cover with portrait of the author" style="background:linear-gradient(135deg,#e9ecef,#d8c9b6 55%,#8fb3cf)"></div>
  <div class="name">Biographies &amp; Memoirs</div><div class="sub">Lorem ipsum</div><div class="line"></div>
</div>

<div class="abs sample" style="left:19px;top:1175px">
  <div class="cover" role="img" aria-label="Meditation album cover with purple mountain landscape" style="background:linear-gradient(180deg,#7b3b8c,#c65bc2 55%,#5c2a6a)"></div>
  <div class="name">Guded Meditations</div><div class="sub">Lorem ipsum</div><div class="line"></div>
</div>
<div class="abs sample" style="left:317px;top:1175px">
  <div class="cover" role="img" aria-label="Business training course cover with portrait of the speaker" style="background:linear-gradient(90deg,#3b2a14,#8a6a34 45%,#6d8fa6)"></div>
  <div class="name">Business Training</div><div class="sub">Lorem ipsum</div><div class="line"></div>
</div>
<div class="abs sample" style="left:613px;top:1175px">
  <div class="cover" role="img" aria-label="Celebrity interview cover with colourful portrait" style="background:linear-gradient(135deg,#2a1010,#c23a3a 45%,#e2c27a 75%,#3a2a20)"></div>
  <div class="name">Celebrity Interviews</div><div class="sub">Lorem ipsum</div><div class="line"></div>
</div>
<div class="abs sample" style="left:911px;top:1175px">
  <div class="cover" role="img" aria-label="Fitness program cover with trainer" style="background:linear-gradient(90deg,#4fb8e0,#7ccbe8 60%,#e7a07a)"></div>
  <div class="name">Fitness Programs</div><div class="sub">Lorem ipsum</div><div class="line"></div>
</div>

<section class="abs band"></section>

<div class="abs point" style="left:19px">
  <h3>Listen your Zelphone, Tabrel or<br>Orbix Device</h3>
  <p>Lorem Ipsum is simply dummy text of the printing and typesetting industry. Lorem Ipsum has been the industry's</p>
</div>
<div class="abs point featured" style="left:427px">
  <h3>All you can enjoy for one low<br>monthly price</h3>
  <p>Lorem Ipsum is simply dummy text of the printing and typesetting industry. Lorem Ipsum has been the industry's</p>
</div>
<div class="abs point" style="left:834px">
  <h3>No Obligation<br>Cancel any time</h3>
  <p>Lorem Ipsum is simply dummy text of the printing and typesetting industry. Lorem Ipsum has been the industry's</p>
</div>

<svg class="abs hex" style="left:160px" viewBox="0 0 62 70" aria-hidden="true">
  <polygon points="31,0 62,17.5 62,52.5 31,70 0,52.5 0,17.5" fill="var(--hex-blue)"/>
  <rect x="16" y="22" width="30" height="26" rx="3" fill="none" stroke="#fff" stroke-width="3"/>
  <rect x="40" y="28" width="3" height="14" fill="#fff"/>
</svg>
<svg class="abs hex" style="left:568px" viewBox="0 0 62 70" aria-hidden="true">
  <polygon points="31,0 62,17.5 62,52.5 31,70 0,52.5 0,17.5" fill="#fff"/>
  <circle cx="31" cy="35" r="15" fill="none" stroke="var(--hex-blue)" stroke-width="3" stroke-dasharray="4 2"/>
  <text x="31" y="42" text-anchor="middle" font-family="PT Sans, sans-serif" font-weight="700" font-size="20" fill="var(--hex-blue)">$</text>
</svg>
<svg class="abs hex" style="left:976px" viewBox="0 0 62 70" aria-hidden="true">
  <polygon points="31,0 62,17.5 62,52.5 31,70 0,52.5 0,17.5" fill="var(--hex-blue)"/>
  <path d="M19 22 L43 48 M43 22 L19 48" stroke="#fff" stroke-width="5" stroke-linecap="round"/>
</svg>

<h2 class="abs section-title trial-title">Start Your Free Trail</h2>
<p class="abs pitch">You will get instant &amp; unlimited access to all the material on Lumawave for 14 days.<br>There is no obligation &amp; you can cancel at any time.</p>
<p class="abs pitch-strong">Credit card Not Required For Free Trail</p>
<div class="abs email">Enter your email address...</div>
<div class="abs btn-access">Get Instant Access</div>
<div class="abs or">— OR —</div>
<div class="abs btn-chat"><span class="mark"></span>Sign Up Using Chatterly</div>

<footer class="abs footer">
  <nav><span>About</span>|<span>Help</span>|<span>Contact Us</span>|<span>Member Login</span>|<span>Privacy Policy</span>|<span>Terms Of Services</span></nav>
  <div>Copyrights © 2014 Lumawave LLC - All Rights Reserved</div>
</footer>

</body>
</html>
```